Cake Bakery needs Large New Vibrant Window Decals

Our cake bakery is moving to a new location. We want to place window decals (vinyl) on 7 separate windows that are all the same size. (Image is attached for your reference. The windows are the ones within the red outline.)

The windows are approximately 76 inches tall and 98 inches wide. We have uploaded an image of the storefront to show you the 7 windows that need be to covered.

There are also 2 side by side doors that need a decals too. We have uploaded a logo we are using. You are allowed to change the logo color to better coordinate with a design you can create.

We want the colors to be bright and cheerful. You can see our current bakery website at brindlewoodsweets.example. ( I included the sign above our bakery if that helps you.)

Do not use any images of cakes or other bakery products in your design.

The graphics can be simple and clean or can be vivid and loud. We will consider all concepts.

You can create one design to be duplicated for each window or create a design that would flow across all the windows in a landscape effect.

Target Market(s)

People who purchase cakes for any occasion.

Industry/Entity Type

Bakery

Requirements
Must have
• Must have the logo on each window
Nice to have
• Open to any concepts
Should not have
• No images of cakes or other bakery products. The graphics must stand the test of time for the next 10 years.

```html
<!DOCTYPE html>
<html lang="en">
<head>
<meta charset="utf-8">
<title>Brindlewood Sweets – Window Decals</title>
<link rel="stylesheet" href="https://fonts.googleapis.com/css2?family=Fredoka:wght@500&display=swap">
<style>
  :root {
    --canvas: #ffffff;
    --lilac: #e6c3ec;
    --blush: #f5a3a6;
    --mint: #33f2c8;
    --salmon: #f3948f;
    --pale-pink: #f9cccc;
    --violet: #b04ed0;
    --coral: #f07f7d;
    --white: #ffffff;
  }
  * { box-sizing: border-box; margin: 0; padding: 0; }
  html, body {
    width: 1200px;
    height: 860px;
    overflow: hidden;
    background: var(--canvas);
  }
  .decal-row {
    position: absolute;
    left: 25px;
    top: 287px;
    display: flex;
    gap: 20px;
  }
  .window-decal {
    position: relative;
    width: 370px;
    height: 286px;
  }
  .window-decal svg {
    position: absolute;
    inset: 0;
    width: 100%;
    height: 100%;
    display: block;
  }
  .decal-name {
    position: absolute;
    left: 0;
    right: 0;
    top: 50%;
    transform: translateY(-50%);
    text-align: center;
    font-family: "Fredoka", sans-serif;
    font-weight: 500;
    font-size: 36px;
    line-height: 1.05;
    color: var(--coral);
  }
</style>
</head>
<body>
  <main class="decal-row">
    <section class="window-decal">
      <svg viewBox="0 0 602 466" preserveAspectRatio="none" aria-hidden="true">
        <rect class="band-top" x="0" y="0" width="602" height="36" fill="var(--lilac)"/>
        <rect x="0" y="22" width="602" height="14" fill="var(--blush)"/>
        <rect class="band-mint" x="0" y="36" width="602" height="40" fill="var(--mint)"/>
        <rect class="band-stripe" x="0" y="76" width="602" height="36" fill="var(--pale-pink)"/>
        <rect class="band-stripe" x="0" y="328" width="602" height="66" fill="var(--pale-pink)"/>
        <rect class="band-mint" x="0" y="394" width="602" height="38" fill="var(--mint)"/>
        <rect x="0" y="432" width="602" height="14" fill="var(--violet)"/>
        <rect class="band-bottom" x="0" y="446" width="602" height="20" fill="var(--lilac)"/>
        <rect class="frame-ornament" x="0" y="100" width="602" height="240" rx="120" fill="var(--salmon)" role="img" aria-label="Decorative scalloped frame with star points"/>
        <rect class="label-field" x="14" y="112" width="574" height="216" rx="108" fill="var(--white)"/>
      </svg>
      <p class="decal-name">Brindlewood<br>Sweets</p>
    </section>
    <section class="window-decal">
      <svg viewBox="0 0 602 466" preserveAspectRatio="none" aria-hidden="true">
        <rect x="0" y="0" width="602" height="36" fill="var(--lilac)"/>
        <rect x="0" y="22" width="602" height="14" fill="var(--blush)"/>
        <rect x="0" y="36" width="602" height="40" fill="var(--mint)"/>
        <rect x="0" y="76" width="602" height="36" fill="var(--pale-pink)"/>
        <rect x="0" y="328" width="602" height="66" fill="var(--pale-pink)"/>
        <rect x="0" y="394" width="602" height="38" fill="var(--mint)"/>
        <rect x="0" y="432" width="602" height="14" fill="var(--violet)"/>
        <rect x="0" y="446" width="602" height="20" fill="var(--lilac)"/>
        <rect x="0" y="100" width="602" height="240" rx="120" fill="var(--salmon)" role="img" aria-label="Decorative scalloped frame with star points"/>
        <rect x="14" y="112" width="574" height="216" rx="108" fill="var(--white)"/>
      </svg>
      <p class="decal-name">Brindlewood<br>Sweets</p>
    </section>
    <section class="window-decal">
      <svg viewBox="0 0 602 466" preserveAspectRatio="none" aria-hidden="true">
        <rect x="0" y="0" width="602" height="36" fill="var(--lilac)"/>
        <rect x="0" y="22" width="602" height="14" fill="var(--blush)"/>
        <rect x="0" y="36" width="602" height="40" fill="var(--mint)"/>
        <rect x="0" y="76" width="602" height="36" fill="var(--pale-pink)"/>
        <rect x="0" y="328" width="602" height="66" fill="var(--pale-pink)"/>
        <rect x="0" y="394" width="602" height="38" fill="var(--mint)"/>
        <rect x="0" y="432" width="602" height="14" fill="var(--violet)"/>
        <rect x="0" y="446" width="602" height="20" fill="var(--lilac)"/>
        <rect x="0" y="100" width="602" height="240" rx="120" fill="var(--salmon)" role="img" aria-label="Decorative scalloped frame with star points"/>
        <rect x="14" y="112" width="574" height="216" rx="108" fill="var(--white)"/>
      </svg>
      <p class="decal-name">Brindlewood<br>Sweets</p>
    </section>
  </main>
</body>
</html>
```